International Wine events organiser seeks simple but stunning business card

I am a freelance events, marketing and PR provider specialised in the Wine industry. I help wineries and wine regions reach trade and consumers in foreign markets through events, help with the websites and communications, press trips and promotional activities. I am looking for a business card which is simple yet effective and is linked to events and communication.

I work mainly - but exclusively - with Italian wineries organising events for them in foreign market.s

I would like to use red in the logo as my present website (lenamorvick.com) used grey and red (although I will be changing the design at a later date).

Target Market(s)

Wine producers, promotional bodies in wine sector, companies looking to hire event organisers,

Industry/Entity Type

Marketing

Requirements
Must have
• My Name - Lena Morvick
My address
My phone
My website : www.lenamorvick.com
my Blog : velvetandtone.me

Should not have
• Butterflies, stars, flowers, anything not particularly linked to wine - would like to keep it simple, modern and eye-catching without being too cliche.

```html
<!DOCTYPE html>
<html lang="en">
<head>
<meta charset="utf-8">
<title>Lena Morvick — Business Card</title>
<link rel="stylesheet" href="https://fonts.googleapis.com/css2?family=Great+Vibes&family=Quicksand:wght@300;400&display=swap">
<style>
  :root {
    --page-bg: #f2f2f2;
    --wine-red: #c8202e;
    --wine-red-light: #e0565c;
    --wine-red-deep: #8a0e1e;
    --charcoal: #3a3a3a;
    --charcoal-dark: #2e2e2e;
    --charcoal-edge: #555555;
    --ink-light: #ffffff;
    --ink-soft: #e6e6e6;
  }
  * { margin: 0; padding: 0; box-sizing: border-box; }
  html, body {
    width: 1200px;
    height: 1000px;
    overflow: hidden;
    background: var(--page-bg);
  }
  .business-card {
    position: absolute;
    left: 100px;
    top: 215px;
    width: 1000px;
    height: 570px;
    overflow: hidden;
    box-shadow: 0 10px 30px rgba(0,0,0,0.25);
  }
  .card-artwork {
    position: absolute;
    inset: 0;
    width: 1000px;
    height: 570px;
  }
  .holder-name {
    position: absolute;
    left: 48px;
    top: 110px;
    font-family: "Great Vibes", cursive;
    font-size: 104px;
    line-height: 1;
    color: var(--ink-light);
    letter-spacing: 1px;
  }
  .postal-address {
    position: absolute;
    left: 52px;
    top: 438px;
    font-family: "Quicksand", sans-serif;
    font-weight: 300;
    font-size: 33px;
    line-height: 38px;
    color: var(--ink-light);
    letter-spacing: 1px;
    font-style: normal;
  }
  .contact-details {
    position: absolute;
    right: 44px;
    top: 360px;
    text-align: right;
    font-family: "Quicksand", sans-serif;
    font-weight: 300;
    color: var(--ink-light);
    letter-spacing: 1px;
  }
  .contact-details .blog { font-size: 19px; color: var(--ink-soft); line-height: 28px; }
  .contact-details .phone { font-size: 30px; line-height: 38px; }
  .contact-details .website { font-size: 24px; line-height: 32px; }
</style>
</head>
<body>
  <div class="business-card">
    <svg class="card-artwork" viewBox="0 0 1000 570" xmlns="http://www.w3.org/2000/svg">
      <defs>
        <linearGradient id="wineField" x1="0" y1="0" x2="1" y2="0">
          <stop offset="0" stop-color="var(--wine-red-deep)"/>
          <stop offset="0.25" stop-color="var(--wine-red)"/>
          <stop offset="0.6" stop-color="var(--wine-red-light)"/>
          <stop offset="0.85" stop-color="var(--wine-red)"/>
          <stop offset="1" stop-color="var(--wine-red-deep)"/>
        </linearGradient>
        <linearGradient id="wineSheen" x1="0" y1="0" x2="0" y2="1">
          <stop offset="0" stop-color="#ffffff" stop-opacity="0.22"/>
          <stop offset="0.5" stop-color="#ffffff" stop-opacity="0.05"/>
          <stop offset="1" stop-color="#000000" stop-opacity="0.1"/>
        </linearGradient>
        <radialGradient id="wineGlow" cx="0.62" cy="0.75" r="0.3">
          <stop offset="0" stop-color="#f3a393" stop-opacity="0.8"/>
          <stop offset="1" stop-color="#f3a393" stop-opacity="0"/>
        </radialGradient>
        <linearGradient id="bottleTone" x1="0" y1="0" x2="1" y2="0">
          <stop offset="0" stop-color="#444444"/>
          <stop offset="1" stop-color="#333333"/>
        </linearGradient>
      </defs>

      <rect class="base-band" width="1000" height="570" fill="var(--charcoal)"/>
      <rect class="wine-field" width="1000" height="470" fill="url(#wineField)"/>
      <rect class="wine-sheen" width="1000" height="470" fill="url(#wineSheen)"/>
      <rect class="wine-glow" width="1000" height="470" fill="url(#wineGlow)"/>

      <path class="lower-band-edge" d="M0 420 C 220 400, 450 360, 660 300 L 1000 300 L 1000 570 L 0 570 Z" fill="var(--charcoal-edge)"/>
      <path class="lower-band" d="M0 430 C 220 410, 450 370, 660 312 L 1000 312 L 1000 570 L 0 570 Z" fill="var(--charcoal)"/>

      <rect class="bottle-group" x="645" y="70" width="320" height="260" fill="url(#bottleTone)"
            role="img" aria-label="Silhouettes of three wine bottles standing in a row"/>
      <rect class="right-edge-strip" x="965" y="230" width="35" height="340" fill="var(--charcoal-dark)"/>
    </svg>

    <div class="holder-name">Lena Morvick</div>

    <address class="postal-address">
      Lena Morvick,<br>
      Lindenhofer Strasse, 52<br>
      80469 Munich
    </address>

    <div class="contact-details">
      <div class="blog">blog.velvetandtone.me</div>
      <div class="phone">Tel: +49 170 5182 634</div>
      <div class="website">lenamorvick.com</div>
    </div>
  </div>
</body>
</html>
```